"Career in Gradvex" | Poster design

We need a "We are hiring" poster design. We are a construction company based in Croatia and we are looking for 3 categories of construction workers. We want moder, serious and powerful poster . In attachment you can find our logo. The font of a text that is used in logo design is "nexa bold".

At the bottom (or where designer can see it) will be description of general condition. The poster must be simple and clear.

Target Market(s)

Wide range of employment

Industry/Entity Type

Construction Company

Colors

Designer to choose colors to be used in the design.

Requirements
Must have
• The text in poster that will be needed is "Mason/carpenter job", "Steel-bender job" and "Auxiliary worker". This terms may be wrong, but it will be translated in local language. Under all of them will be a short descrtiption row, and one row of salary. This is for all three categories.
• At the bottom (or where designer can see it) will be description of general condition. The poster must be simple and clear.

```html
<!DOCTYPE html>
<html lang="hr">
<head>
<meta charset="utf-8">
<title>Gradvex – We are hiring</title>
<link rel="stylesheet" href="https://fonts.googleapis.com/css2?family=Montserrat:wght@300;700&family=Figtree:wght@500;700&display=swap">
<style>
  :root {
    --orange: #e8913f;
    --ink: #1c1c1c;
    --grey: #5e5e5e;
    --paper: #ffffff;
    --backdrop: #ececec;
  }
  * { margin: 0; padding: 0; box-sizing: border-box; }
  html, body { width: 1000px; height: 1200px; overflow: hidden; }
  body { background: var(--backdrop); position: relative; }

  .poster {
    position: absolute; left: 112px; top: 20px;
    width: 776px; height: 1160px;
    background: var(--paper);
    border: 22px solid var(--orange);
    text-align: center;
    color: var(--ink);
  }
  .brand {
    position: absolute; left: 0; right: 0; top: 170px;
  }
  .brand-name {
    font-family: "Figtree", sans-serif; font-weight: 700;
    font-size: 96px; line-height: 1; letter-spacing: 2px;
    color: var(--orange); text-transform: uppercase;
  }
  .brand-tagline {
    margin-top: 14px;
    font-family: "Figtree", sans-serif; font-weight: 500;
    font-size: 18px; letter-spacing: 0.5px; color: var(--grey);
  }
  .headline { position: absolute; left: 0; right: 0; top: 420px; }
  .headline-lead {
    font-family: "Montserrat", sans-serif; font-weight: 300;
    font-size: 92px; line-height: 1; color: var(--ink);
  }
  .headline-main {
    font-family: "Montserrat", sans-serif; font-weight: 700;
    font-size: 148px; line-height: 1; margin-top: 14px;
    color: var(--orange); letter-spacing: -2px;
  }
  .positions {
    position: absolute; left: 0; right: 0; top: 688px;
    list-style: none;
    font-family: "Figtree", sans-serif; font-weight: 700;
    font-size: 48px; line-height: 76px;
  }
  .details {
    position: absolute; left: 106px; width: 520px; top: 914px; height: 60px;
    background: var(--orange); color: var(--ink);
    font-family: "Figtree", sans-serif; font-weight: 500; font-size: 18px;
    display: flex; align-items: center; justify-content: center;
  }
  .call-band {
    position: absolute; left: 0; right: 0; bottom: 0; height: 110px;
    background: var(--ink); color: var(--paper);
    font-family: "Figtree", sans-serif; font-weight: 700; font-size: 46px;
    display: flex; align-items: center; justify-content: center;
  }
</style>
</head>
<body>
  <article class="poster">
    <header class="brand">
      <div class="brand-name">Gradvex</div>
      <div class="brand-tagline">IZVOĐENJE I VOĐENJE GRAĐEVINSKIH RADOVA</div>
    </header>
    <section class="headline">
      <div class="headline-lead">WE ARE</div>
      <div class="headline-main">HIRING</div>
    </section>
    <ul class="positions">
      <li>Mason/carpenter</li>
      <li>Steel-bender</li>
      <li>Auxiliary worker</li>
    </ul>
    <p class="details">short descrtiption row, and one row of salary</p>
    <footer class="call-band">CALL NOW - 0987 654 321</footer>
  </article>
</body>
</html>
```